New Solo Law Office Needs Business Card/Letterhead Design

I am starting a solo law office called "Law Office of Conrad Vashti, PLLC" in Saguaro Flats, Arizona. I will be doing criminal defense trial work. More than a logo with any sort of icon, I am really just looking for the name of the company to be displayed in a sleek, minimalist but interesting sort of way, with a format and font type that communicates professionalism. It can be in color, but doesn't have to be, and I am thinking blue and/or red accents colors. I'd like it to convey that I am passionate, dependable and willing to fight. For the business card, I envision sort of higher quality card material, and maybe some embossing or raised print. I will want to include my company name, name, phone and fax numbers, email and website addresses. For the letterhead, I will want to be able to use the same sort of font/formatting design as on the business card.
Industry/Entity Type
Business
Contact Information for Business Card
Law Office of Conrad Vashti, PLLC
Conrad Vashti
conrad@vashti-law.example
www.vashti-law.example
(I do not yet have an established phone or fax number, so please put in some place holder numbers for the formatting, and I can add the actual numbers in before I print.)
Colors
Designer to choose colors to be used in the design.
Look and feel

```html
<!DOCTYPE html>
<html lang="en">
<head>
<meta charset="utf-8">
<title>Law Office of Conrad Vashti, PLLC — Business Card</title>
<link href="https://fonts.googleapis.com/css2?family=Cinzel:wght@400;600&family=Roboto:wght@400&display=swap" rel="stylesheet">
<style>
  :root {
    --firm-red: #b51f24;
    --firm-red-tint: #c0302f;
    --firm-navy: #23248a;
    --ink: #1a1a1a;
    --card-white: #ffffff;
    --watermark: #ececec;
    --rule: #cfcfcf;
    --backdrop: #e4e4e6;
  }
  html, body {
    margin: 0;
    padding: 0;
    width: 1200px;
    height: 900px;
    overflow: hidden;
    background: var(--backdrop);
  }
  .canvas {
    position: relative;
    width: 1200px;
    height: 900px;
  }
  .card {
    position: absolute;
    width: 640px;
    height: 366px;
    left: 280px;
    border-radius: 22px;
    overflow: hidden;
    box-shadow: 0 10px 28px rgba(0,0,0,0.18);
  }
  .card--back {
    top: 50px;
    background: var(--firm-red);
  }
  .card--front {
    top: 480px;
    background: var(--card-white);
  }
  .watermark-disc {
    position: absolute;
    border-radius: 50%;
  }
  .card--back .watermark-disc {
    width: 340px;
    height: 340px;
    right: -20px;
    top: 30px;
    background: var(--firm-red-tint);
  }
  .card--front .watermark-disc {
    width: 300px;
    height: 300px;
    left: 0;
    top: 30px;
    background: var(--watermark);
  }
  .firm-lockup {
    position: absolute;
    display: flex;
    align-items: center;
    gap: 16px;
  }
  .firm-mark {
    flex: none;
    border-radius: 50%;
  }
  .firm-name {
    margin: 0;
    font-family: "Cinzel", "Times New Roman", serif;
    font-weight: 400;
    line-height: 1.15;
    letter-spacing: 0.04em;
    text-transform: uppercase;
    white-space: nowrap;
  }
  .card--back .firm-lockup {
    left: 120px;
    top: 147px;
  }
  .card--back .firm-mark {
    width: 72px;
    height: 72px;
    background: var(--card-white);
  }
  .card--back .firm-name {
    color: var(--card-white);
    font-size: 30px;
    padding-left: 16px;
    border-left: 1px solid rgba(255,255,255,0.6);
  }
  .attorney {
    position: absolute;
    left: 40px;
    top: 200px;
  }
  .attorney-name {
    font-family: "Cinzel", "Times New Roman", serif;
    font-weight: 600;
    font-size: 25px;
    color: var(--firm-navy);
    letter-spacing: 0.03em;
    text-transform: uppercase;
    white-space: nowrap;
    margin: 0;
  }
  .attorney-title {
    font-family: "Cinzel", "Times New Roman", serif;
    font-size: 13px;
    color: var(--firm-red);
    letter-spacing: 0.08em;
    text-transform: uppercase;
    margin: 4px 0 0;
  }
  .front-panel {
    position: absolute;
    left: 318px;
    top: 58px;
    padding-left: 20px;
    border-left: 1px solid var(--rule);
  }
  .card--front .firm-lockup {
    position: static;
    gap: 12px;
    margin-bottom: 22px;
  }
  .card--front .firm-mark {
    width: 42px;
    height: 42px;
    background: var(--firm-red);
  }
  .card--front .firm-name {
    color: var(--firm-navy);
    font-size: 17px;
  }
  .contact-list {
    list-style: none;
    margin: 0;
    padding: 0;
    font-family: "Roboto", Arial, sans-serif;
    font-size: 17px;
    color: var(--ink);
  }
  .contact-list li {
    display: flex;
    align-items: center;
    gap: 12px;
    height: 30px;
    white-space: nowrap;
  }
  .contact-icon {
    width: 17px;
    height: 17px;
    flex: none;
    fill: var(--firm-red);
  }
  .contact-icon--line {
    fill: none;
    stroke: var(--firm-red);
    stroke-width: 2;
  }
</style>
</head>
<body>
<main class="canvas">

  <section class="card card--back" aria-label="Business card back">
    <div class="watermark-disc" aria-hidden="true"></div>
    <div class="firm-lockup">
      <span class="firm-mark" aria-hidden="true"></span>
      <p class="firm-name">Law Office of<br>Conrad Vashti, PLLC</p>
    </div>
  </section>

  <section class="card card--front" aria-label="Business card front">
    <div class="watermark-disc" aria-hidden="true"></div>

    <div class="attorney">
      <h1 class="attorney-name">Conrad Vashti</h1>
      <p class="attorney-title">Attorney at Law</p>
    </div>

    <div class="front-panel">
      <div class="firm-lockup">
        <span class="firm-mark" aria-hidden="true"></span>
        <p class="firm-name">Law Office of<br>Conrad Vashti, PLLC</p>
      </div>

      <ul class="contact-list">
        <li>
          <svg class="contact-icon" viewBox="0 0 24 24" aria-label="Phone"><path d="M3 8c0-2 2-4 9-4s9 2 9 4v2h-5V8H8v2H3zM6 11h12l2 8H4z"/></svg>
          520-555-0147
        </li>
        <li>
          <svg class="contact-icon" viewBox="0 0 24 24" aria-label="Fax"><path d="M7 3h10v5H7zM3 9h18v8h-4v4H7v-4H3zm6 6v4h6v-4z"/></svg>
          520-555-0193
        </li>
        <li>
          <svg class="contact-icon" viewBox="0 0 24 24" aria-label="Location"><path d="M12 2a7 7 0 0 1 7 7c0 5-7 13-7 13S5 14 5 9a7 7 0 0 1 7-7zm0 4a3 3 0 1 0 0 6 3 3 0 0 0 0-6z"/></svg>
          Saguaro Flats, Arizona
        </li>
        <li>
          <svg class="contact-icon" viewBox="0 0 24 24" aria-label="Email"><path d="M2 5h20v14H2zm2 2v.5l8 5.5 8-5.5V7zm0 3v7h16v-7l-8 5.5z"/></svg>
          conrad@vashti-law.example
        </li>
        <li>
          <svg class="contact-icon contact-icon--line" viewBox="0 0 24 24" aria-label="Website"><circle cx="12" cy="12" r="9"/><ellipse cx="12" cy="12" rx="4" ry="9"/><path d="M3 12h18M5 7h14M5 17h14"/></svg>
          www.vashti-law.example
        </li>
      </ul>
    </div>
  </section>

</main>
</body>
</html>
```